Business card design needed for Automotive Reconditioning business

I have a logo design i just cant decide on the best color or layout for the business card, I will upload all the files so you can see all colors schemes we are considering. I have other file formats if needed let me know.

Target Market(s)

automotive dealerships

Contact Information for Business Card

HERE are the Descriptions and info needed on the card:
Interior Repair: Leather carpet burns panels dash Deoderize
Dealer products and Vin Verify
( spot for name and cell number) My name is Norman Bexley phone 614 352-4180 Title COO www.QuorvalMotive.com

Font styles to use
Sans Serif
Other font styles liked:
• what ever you think looks best

Requirements
Must have
• Must be able to change the name and phone for employees

```html
<!DOCTYPE html>
<html lang="en">
<head>
<meta charset="utf-8">
<title>Quorval Motive – Business Card</title>
<link rel="stylesheet" href="https://fonts.googleapis.com/css2?family=Montserrat:wght@300;400;600;800&display=swap">
<style>
  :root {
    --stage: #34363b;
    --card-dark: #272b36;
    --blue-deep: #1d4aa8;
    --blue-mid: #1f66c4;
    --blue-light: #1e86da;
    --red-orange: #ec4a26;
    --red-bright: #e5272f;
    --red-mid: #d4222b;
    --red-deep: #b51c24;
    --red-darker: #9e1820;
    --text-light: #ffffff;
    --text-soft: #f6c9bf;
  }
  * { box-sizing: border-box; margin: 0; padding: 0; }
  html, body {
    width: 1200px; height: 900px; overflow: hidden;
    background: var(--stage);
    font-family: "Montserrat", sans-serif;
  }
  .stage { position: relative; width: 1200px; height: 900px; }
  .card {
    position: absolute; top: 155px;
    width: 340px; height: 590px;
    border-radius: 22px; overflow: hidden;
    background: var(--card-dark);
    box-shadow: 0 14px 30px rgba(0,0,0,.35);
  }
  .card--front { left: 220px; }
  .card--back { left: 640px; }

  .tabs-blue { position: absolute; top: 0; left: 38px; width: 92px; }
  .tabs-blue span { display: block; height: 34px; }
  .tabs-blue span:nth-child(1) { background: var(--blue-deep); }
  .tabs-blue span:nth-child(2) { background: var(--blue-mid); }
  .tabs-blue span:nth-child(3) { background: var(--blue-light); }

  .brand {
    position: absolute; left: 0; right: 0;
    display: flex; align-items: center; justify-content: center; gap: 10px;
  }
  .brand__mark { width: 14px; height: 14px; background: var(--blue-light); }
  .brand__name {
    font-weight: 800; font-size: 26px; letter-spacing: 1px;
    color: var(--red-bright); text-transform: uppercase;
  }
  .card--front .brand { top: 142px; }

  /* front red section */
  .contact { position: absolute; top: 210px; left: 0; right: 0; bottom: 0; }
  .contact__head {
    height: 110px; background: var(--red-orange);
    padding: 34px 0 0 0; text-align: center; color: var(--text-light);
  }
  .contact__name { font-size: 21px; letter-spacing: .5px; }
  .contact__name b { font-weight: 800; }
  .contact__name span { font-weight: 300; }
  .contact__title { font-size: 12px; font-weight: 400; color: var(--text-soft); letter-spacing: 2px; margin-top: 4px; }

  .row { display: flex; height: 90px; }
  .row__icon {
    width: 78px; display: flex; align-items: center; justify-content: center;
  }
  .row__icon svg { width: 20px; height: 20px; fill: var(--text-light); }
  .row__text {
    flex: 1; display: flex; flex-direction: column; justify-content: center;
    padding-left: 20px; color: var(--text-light);
    font-size: 14px; font-weight: 400; line-height: 1.45;
  }
  .row--address .row__icon { background: var(--red-darker); }
  .row--address .row__text { background: var(--red-bright); }
  .row--phone .row__icon { background: var(--red-bright); }
  .row--phone .row__text { background: var(--red-deep); font-size: 16px; letter-spacing: 1px; }
  .row--web .row__icon { background: var(--red-mid); }
  .row--web .row__text { background: var(--red-deep); }
  .row--web { height: 100px; }

  /* back */
  .card--back .brand { top: 262px; }
  .car-outline {
    position: absolute; left: 60px; top: 190px; width: 220px; height: 180px;
    background: radial-gradient(ellipse at center, rgba(0,0,0,.22), rgba(0,0,0,0) 70%);
  }
  .card--back .url {
    position: absolute; left: 30px; bottom: 46px; width: 165px;
    color: var(--text-light); font-size: 13px; font-weight: 400; letter-spacing: .4px;
    white-space: nowrap;
  }
  .tabs-red { position: absolute; bottom: 0; right: 38px; width: 92px; }
  .tabs-red span { display: block; height: 40px; }
  .tabs-red span:nth-child(1) { background: var(--red-darker); }
  .tabs-red span:nth-child(2) { background: var(--red-deep); }
  .tabs-red span:nth-child(3) { background: var(--red-bright); }
  .tabs-red span:nth-child(4) { background: var(--red-orange); }
</style>
</head>
<body>
<main class="stage">

  <section class="card card--front">
    <div class="tabs-blue"><span></span><span></span><span></span></div>
    <div class="brand">
      <span class="brand__mark"></span>
      <span class="brand__name">Quorval Motive</span>
    </div>
    <div class="contact">
      <div class="contact__head">
        <p class="contact__name"><b>NORMAN</b> <span>BEXLEY</span></p>
        <p class="contact__title">COO</p>
      </div>
      <div class="row row--address">
        <div class="row__icon">
          <svg viewBox="0 0 24 24" aria-hidden="true"><path d="M12 2a7 7 0 0 0-7 7c0 5 7 13 7 13s7-8 7-13a7 7 0 0 0-7-7zm0 9.5A2.5 2.5 0 1 1 12 6.5a2.5 2.5 0 0 1 0 5z"/></svg>
        </div>
        <div class="row__text"><span>Your address here</span><span>single or double line</span></div>
      </div>
      <div class="row row--phone">
        <div class="row__icon">
          <svg viewBox="0 0 24 24" aria-hidden="true"><path d="M6.6 10.8a15 15 0 0 0 6.6 6.6l2.2-2.2c.3-.3.7-.4 1-.2 1.1.4 2.3.6 3.6.6.6 0 1 .4 1 1V20c0 .6-.4 1-1 1A17 17 0 0 1 3 4c0-.6.4-1 1-1h3.5c.6 0 1 .4 1 1 0 1.3.2 2.5.6 3.6.1.3 0 .7-.2 1z"/></svg>
        </div>
        <div class="row__text">614 352-4180</div>
      </div>
      <div class="row row--web">
        <div class="row__icon">
          <svg viewBox="0 0 24 24" aria-hidden="true"><path d="M12 2a10 10 0 1 0 0 20 10 10 0 0 0 0-20zm6.9 6h-3a15 15 0 0 0-1.3-3.7A8 8 0 0 1 18.9 8zM12 4c.8 1.2 1.5 2.5 1.9 4h-3.8c.4-1.5 1.1-2.8 1.9-4zM4.3 14a8 8 0 0 1 0-4h3.4a16 16 0 0 0 0 4zm.8 2h3a15 15 0 0 0 1.3 3.7A8 8 0 0 1 5.1 16zm3-8h-3a8 8 0 0 1 4.3-3.7C8.8 5.5 8.4 6.7 8.1 8zM12 20c-.8-1.2-1.5-2.5-1.9-4h3.8c-.4 1.5-1.1 2.8-1.9 4zm2.3-6H9.7a14 14 0 0 1 0-4h4.6a14 14 0 0 1 0 4zm.3 5.7c.6-1.1 1-2.4 1.3-3.7h3a8 8 0 0 1-4.3 3.7zm1.7-5.7a16 16 0 0 0 0-4h3.4a8 8 0 0 1 0 4z"/></svg>
        </div>
        <div class="row__text"><span>www.QuorvalMotive.com</span><span>norman@quorvalmotive.com</span></div>
      </div>
    </div>
  </section>

  <section class="card card--back">
    <div class="tabs-blue"><span></span><span></span><span></span></div>
    <div class="car-outline" role="img" aria-label="Faint outline drawing of a car behind the company name"></div>
    <div class="brand">
      <span class="brand__mark"></span>
      <span class="brand__name">Quorval Motive</span>
    </div>
    <p class="url">quorvalmotive.com</p>
    <div class="tabs-red"><span></span><span></span><span></span><span></span></div>
  </section>

</main>
</body>
</html>
```